Everett's Book Cover

Need a cover design for a book (paperback and eBook)
Book Title: Where The Cedar Rivers Bend
Book Width: 15.24
Book Height: 22.86
Thickness: approximately 200 pages.
Book is a collection of stories drawn from the author's life, and will be in the local history genre in northern British Columbia, Canada from the period 1930 to the present time.
Author: Everett Hollis Pelletier
Must include "As told to Marnie Kowal" on front cover, not on the spine.
Author invites designers creativity and asks that the attached photos be incorporated into the front and back covers in tasteful ways as follows:
Other uses of the photos will be considered.
We apologize for the quality of the photos. Please do what you can.
We look forward to your designs.
Thank you for considering.

Target Market(s)

Lovers of local history, jokes, storytelling, back country hiking and mountain climbing. Men and women 30 years and older. Primary target readership are men and women in their 40's, 50's, 60's, and older, who love local history

Font styles to use
Sans Serif

Requirements
Must have
• Back cover copy must clear and easy to read.
Must appeal to outdoor, back country types.
Nice to have
• Like to see a creative incorporation of the photos provided.
Build on or compliment the colours in the photos

```html
<!DOCTYPE html>
<html lang="en">
<head>
<meta charset="utf-8">
<title>Where The Cedar Rivers Bend – Book Cover</title>
<link rel="stylesheet" href="https://fonts.googleapis.com/css2?family=Barlow+Condensed:wght@500;600;700&display=swap">
<style>
  :root{
    --page:#ffffff;
    --ink:#2a2016;
    --white:#ffffff;
    --gold:#f2c230;
    --sky-top:#3b78c0;
    --sky-mid:#a9cbe6;
    --ridge:#8f9c98;
    --meadow:#9aa84c;
    --meadow-warm:#c2b24a;
    --earth:#7a4c22;
    --frame:#ffffff;
  }
  html,body{margin:0;padding:0;width:1200px;height:1000px;overflow:hidden;background:var(--page);}
  .canvas{position:relative;width:1200px;height:1000px;font-family:"Barlow Condensed","Arial Narrow",sans-serif;}
  .spread{position:absolute;left:18px;top:22px;width:1164px;height:840px;overflow:hidden;}

  .front-photo{position:absolute;left:400px;top:0;width:764px;height:840px;
    background:
      radial-gradient(ellipse 420px 120px at 560px 200px, rgba(255,255,255,.75), rgba(255,255,255,0) 70%),
      radial-gradient(ellipse 300px 90px at 150px 310px, rgba(255,255,255,.8), rgba(255,255,255,0) 70%),
      linear-gradient(180deg,var(--sky-top) 0%,#6d9dd2 18%,var(--sky-mid) 36%,#d9e4ea 42%,var(--ridge) 46%,#7f9a5a 50%,var(--meadow) 58%,var(--meadow-warm) 74%,#a57a34 88%,var(--earth) 100%);}

  .back-paper{position:absolute;left:0;top:0;width:470px;height:840px;}

  .back-title{position:absolute;left:56px;top:58px;margin:0;color:rgba(255,255,255,.92);text-transform:uppercase;line-height:.88;}
  .back-title .big{display:block;font-size:96px;font-weight:700;letter-spacing:1px;}
  .back-title .small{display:block;font-size:27px;font-weight:600;margin-top:2px;color:var(--white);}

  .photo-frame{position:absolute;background:var(--frame);padding:8px;box-shadow:2px 4px 10px rgba(0,0,0,.35);}
  .photo-frame .fill{width:100%;height:100%;}
  .bear-photo{left:330px;top:26px;width:186px;height:152px;transform:rotate(5deg);}
  .bear-photo .fill{background:linear-gradient(160deg,#b7a07a,#8c7a4a 45%,#c8c2b0 70%,#6e7a3c);}
  .couple-photo{left:55px;top:505px;width:140px;height:168px;}
  .couple-photo .fill{background:linear-gradient(180deg,#4e7a48 0%,#6e9a5a 40%,#3c5a8a 60%,#8aa860 100%);}

  .back-copy{position:absolute;color:var(--ink);font-size:14.2px;font-weight:600;line-height:21.5px;margin:0;}
  .copy-one{left:55px;top:214px;width:370px;}
  .copy-two{left:55px;top:390px;width:370px;}
  .copy-three{left:235px;top:504px;width:165px;line-height:23px;}

  .spine-text{position:absolute;left:577px;top:16px;transform-origin:0 0;transform:rotate(90deg) translateY(-100%);white-space:nowrap;text-transform:uppercase;width:820px;display:flex;align-items:baseline;}
  .spine-title{font-size:29px;font-weight:600;color:var(--white);letter-spacing:.5px;}
  .spine-author{font-size:29px;font-weight:700;color:var(--white);margin-left:96px;}

  .front-title{position:absolute;left:620px;top:58px;width:520px;margin:0;text-align:center;text-transform:uppercase;line-height:.85;}
  .front-title .big{display:block;font-size:178px;font-weight:700;letter-spacing:2px;color:rgba(255,255,255,.82);}
  .front-title .small{display:block;font-size:57px;font-weight:700;color:var(--white);margin-top:8px;text-shadow:0 1px 4px rgba(0,0,0,.25);}

  .tagline{position:absolute;right:60px;top:418px;width:160px;margin:0;text-align:right;color:var(--white);font-size:21px;font-weight:600;line-height:23px;text-shadow:0 1px 3px rgba(0,0,0,.4);}
  .tagline strong{color:var(--gold);font-size:27px;line-height:27px;font-weight:700;}
  .swoosh{position:absolute;left:992px;top:628px;}

  .front-author{position:absolute;left:620px;top:706px;width:520px;text-align:center;color:var(--white);text-transform:uppercase;font-size:44px;font-weight:700;text-shadow:0 2px 5px rgba(0,0,0,.4);}
  .front-credit{position:absolute;left:620px;top:760px;width:520px;text-align:center;color:var(--white);text-transform:uppercase;font-size:19px;font-weight:700;text-shadow:0 1px 4px rgba(0,0,0,.4);}
  .front-credit b{color:var(--gold);font-size:27px;}
</style>
</head>
<body>
<div class="canvas">
  <div class="spread">
    <div class="front-photo" role="img" aria-label="Photograph of a hiker with a backpack crossing an alpine meadow of wildflowers below snow-patched mountains and a cloudy blue sky"></div>

    <svg class="back-paper" viewBox="0 0 470 840" aria-hidden="true">
      <defs>
        <linearGradient id="kraftTone" x1="0" y1="0" x2="1" y2="1">
          <stop offset="0" stop-color="#dcc69b"/>
          <stop offset=".5" stop-color="#e8d6b0"/>
          <stop offset="1" stop-color="#d3b98a"/>
        </linearGradient>
      </defs>
      <path d="M0 0 H420 L424 30 L416 62 L428 95 L419 130 L432 168 L424 210 L438 250 L428 290 L441 330 L432 372 L445 410 L436 452 L448 495 L438 540 L450 585 L441 630 L453 672 L444 715 L456 760 L447 800 L452 840 H0 Z" fill="url(#kraftTone)"/>
      <path d="M420 0 L424 30 L416 62 L428 95 L419 130 L432 168 L424 210 L438 250 L428 290 L441 330 L432 372 L445 410 L436 452 L448 495 L438 540 L450 585 L441 630 L453 672 L444 715 L456 760 L447 800 L452 840" fill="none" stroke="#f4ead6" stroke-width="4"/>
    </svg>

    <h2 class="back-title"><span class="big">Where</span><span class="small">The Cedar Rivers Bend</span></h2>

    <div class="photo-frame bear-photo"><div class="fill" role="img" aria-label="Photograph of a grizzly bear standing in a meadow with patches of snow"></div></div>

    <p class="back-copy copy-one">Everett Pelletier is a true old-fashioned story teller. He loves nothing better than a good story, and particularly when he is the one telling the story. He was born and raised in the tiny sawmill town of Alder Flats, BC and spent 80 years of his life there before relocating to his current home on the banks of the Sorrel River in Fort Marlow, BC. In addition to writing this book, Everett spends his time writing songs, singing, telling jokes, and entertaining his many friends with stories of days gone by.</p>

    <p class="back-copy copy-two">At the age of 15 he started his career as a flunky in the cookhouse, then moved on to work as a horse logger, sawmill worker, bush foreman, rancher, cat skinner, forest warden, road and bridge builder, and finished his career as salmon hatchery manager.</p>

    <div class="photo-frame couple-photo"><div class="fill" role="img" aria-label="Photograph of the author and his wife standing together in a mountain wildflower meadow"></div></div>

    <p class="back-copy copy-three">Everett’s love of the mountains is evident throughout the book, as is his love for the majestic grizzly bears who inhabit them. He spent his spare time mountain climbing, fishing, skiing, snowshoeing, and hiking in the woods near his home.</p>

    <div class="spine-text">
      <span class="spine-title">Where The Cedar Rivers Bend</span>
      <span class="spine-author">Everett Hollis Pelletier</span>
    </div>

    <h1 class="front-title"><span class="big">Where</span><span class="small">The Cedar Rivers Bend</span></h1>

    <p class="tagline">An eclectic collection of stories about <strong>family, friends, and adventures,</strong> all sprinkled with the author’s unique sense of humour.</p>
    <svg class="swoosh" width="110" height="16" viewBox="0 0 110 16" aria-hidden="true"><path d="M2 12 Q55 2 108 8" fill="none" stroke="var(--gold)" stroke-width="4" stroke-linecap="round"/></svg>

    <div class="front-author">Everett Hollis Pelletier</div>
    <div class="front-credit">As told to <b>Marnie Kowal</b></div>
  </div>
</div>
</body>
</html>
```